Bluecrest Wound Care and Hyperbarics Website Refresh

I want to revamp my current website to be more streamlined and look cleaner. I am also adding additional service lines and another location to the company so I would like that added as well. I want to stick with the same logo and colors, but just have it cleaned up with a better overall design.

www.bchyperbarics-demo.com

Target Market(s)

Wound Care and Hyperbaric Patients

Industry/Entity Type

Healthcare

Coding

Coded - Design and coding required

Number of Pages Required

5+ page

Colors
0054AA
0677BA
7BADD7
CADEEF
E8F1F8
59FF00
82FF00
B8FF75
E3FFCB
F4FFEA

```html
<!DOCTYPE html>
<html lang="en">
<head>
<meta charset="utf-8">
<title>Bluecrest Wound Care and Hyperbarics</title>
<link rel="stylesheet" href="https://fonts.googleapis.com/css2?family=Jost:wght@400;500;600&family=Montserrat:wght@600;700;800&family=Poppins:ital,wght@0,400;0,500;0,600;1,400&display=swap">
<style>
:root{
  --blue-deep:#0054AA;
  --blue:#0677BA;
  --blue-soft:#7BADD7;
  --blue-pale:#CADEEF;
  --blue-mist:#E8F1F8;
  --lime:#82FF00;
  --lime-soft:#B8FF75;
  --navy:#0b2d55;
  --navy-dark:#082444;
  --ink:#1f2a37;
  --grey-text:#4a4f57;
  --field-border:#9aa7b5;
  --white:#ffffff;
}
*{box-sizing:border-box;margin:0;padding:0}
html,body{width:1200px;height:3900px;overflow:hidden;background:var(--white)}
body{position:relative;font-family:"Poppins",sans-serif;color:var(--ink)}
.btn{position:absolute;display:flex;align-items:center;justify-content:center;background:var(--blue);color:var(--white);font-family:"Poppins",sans-serif;font-weight:600;font-size:16px;border-radius:4px}
.photo{position:absolute;overflow:hidden}

/* header */
.brand{position:absolute;left:171px;top:24px;font-family:"Montserrat",sans-serif;font-weight:700;font-size:40px;letter-spacing:1px;color:var(--ink);line-height:1}
.brand-sub{position:absolute;left:236px;top:64px;font-family:"Poppins",sans-serif;font-weight:600;font-size:12px;color:var(--ink)}
.top-strip{position:absolute;left:880px;top:0;width:320px;height:32px}
.social-dot{position:absolute;top:8px;width:14px;height:14px;border-radius:50%;background:var(--white)}
.nav-link{position:absolute;top:56px;font-weight:500;font-size:15px;color:var(--ink)}
.nav-active{position:absolute;left:641px;top:80px;width:14px;height:14px;border:3px solid var(--blue-deep);border-radius:50%}

/* hero */
.hero-kicker{position:absolute;left:169px;top:184px;font-family:"Montserrat",sans-serif;font-weight:600;font-size:21px;letter-spacing:5px;color:var(--blue-deep)}
.hero-title{position:absolute;left:168px;top:222px;font-family:"Montserrat",sans-serif;font-weight:800;font-size:60px;line-height:84px;letter-spacing:0.5px;color:var(--ink)}
.hero-sub{position:absolute;left:170px;top:396px;font-size:22px;color:var(--ink)}
.slider-dot{position:absolute;top:611px;width:17px;height:17px;border-radius:50%;border:2px solid var(--blue)}
.slider-dot.is-active{background:var(--blue)}
.hero-art{position:absolute;left:480px;top:100px;width:560px;height:560px}
.hero-photo{left:552px;top:163px;width:424px;height:424px;border-radius:50%;background:linear-gradient(150deg,#d9dde2,#f2f2f0 45%,#b7aaa2)}

/* welcome */
.welcome-photo{left:171px;top:719px;width:404px;height:372px;border-radius:50px;background:linear-gradient(160deg,#cfd2d0,#9aa19c 45%,#e9e6e1)}
.welcome-pre{position:absolute;left:608px;top:740px;font-family:"Jost",sans-serif;font-size:29px;color:var(--ink)}
.welcome-title{position:absolute;left:606px;top:774px;font-family:"Montserrat",sans-serif;font-weight:700;font-size:52px;letter-spacing:1px;color:var(--ink)}
.welcome-copy{position:absolute;left:608px;top:852px;width:430px;font-size:14px;line-height:27px;color:var(--grey-text)}

/* call band */
.call-band{position:absolute;left:0;top:1165px;width:1200px;height:481px;background:var(--navy);border-top-left-radius:90px}
.call-title{position:absolute;left:171px;top:1312px;font-family:"Jost",sans-serif;font-weight:500;font-size:35px;color:var(--white)}
.call-title span{color:var(--lime);font-weight:600}
.call-sub{position:absolute;left:171px;top:1368px;font-family:"Jost",sans-serif;font-size:21px;color:var(--white)}
.call-number{position:absolute;left:170px;top:1406px;font-family:"Jost",sans-serif;font-weight:600;font-size:40px;color:var(--white)}
.frame{position:absolute;border-top:2px solid var(--blue-soft);border-right:2px solid var(--blue-soft);border-top-right-radius:40px}
.call-photo{left:623px;top:1259px;width:406px;height:315px;border-radius:40px 40px 0 40px;background:linear-gradient(135deg,#e6e6e6,#c9c2bb 40%,#d98a3a 80%)}

/* team */
.team-section{position:absolute;left:0;top:1646px;width:1200px;height:664px;background:var(--white);border-bottom-right-radius:150px;z-index:2}
.blue-corner{position:absolute;right:0;top:2160px;width:200px;height:200px;background:var(--blue)}
.team-photo{top:1714px;width:396px;height:298px;border-radius:40px 0 0 40px;z-index:3}
.team-name{position:absolute;top:2036px;font-family:"Jost",sans-serif;font-weight:500;font-size:26px;color:var(--ink);z-index:3}
.team-role{position:absolute;top:2074px;font-style:italic;font-weight:500;font-size:14px;color:var(--ink);z-index:3}
.team-copy{position:absolute;font-size:13px;line-height:24px;color:var(--grey-text);z-index:3}

/* news */
.news-band{position:absolute;left:0;top:2310px;width:1200px;height:720px;background:linear-gradient(160deg,#0677BA 0%,#0565a8 45%,#0054AA 100%);border-top-left-radius:90px}
.news-heading{position:absolute;left:0;top:2354px;width:1200px;text-align:center;font-family:"Jost",sans-serif;font-weight:500;font-size:45px;color:var(--white)}
.news-photo{top:2433px;width:269px;height:181px;border-radius:10px}
.news-title{position:absolute;top:2624px;width:284px;font-family:"Jost",sans-serif;font-weight:500;font-size:21px;line-height:31px;color:var(--white)}
.news-copy{position:absolute;top:2722px;width:270px;font-size:13px;line-height:22px;color:var(--white)}
.news-btn{position:absolute;top:2829px;width:150px;height:44px;border:2px solid var(--white);border-radius:4px;display:flex;align-items:center;justify-content:center;font-weight:600;font-size:16px;color:var(--white)}

/* contact */
.contact-section{position:absolute;left:0;top:2943px;width:1200px;height:547px;background:var(--blue-mist);border-top-left-radius:90px;border-bottom-right-radius:120px;z-index:2}
.footer-corner{position:absolute;right:0;top:3380px;width:200px;height:160px;background:var(--navy)}
.contact-heading{position:absolute;left:171px;top:3022px;font-family:"Jost",sans-serif;font-weight:500;font-size:38px;color:var(--ink);z-index:3}
.field{position:absolute;border:1.5px solid var(--field-border);border-radius:3px;background:var(--white);font-size:13px;color:var(--ink);padding:14px 12px;z-index:3}
.contact-photo{left:749px;top:3064px;width:268px;height:333px;border-radius:40px 40px 0 40px;background:linear-gradient(135deg,#ece9e6,#d7c6b8 50%,#b7443a 90%);z-index:3}

/* footer */
.site-footer{position:absolute;left:0;top:3488px;width:1200px;height:412px;background:linear-gradient(160deg,var(--navy),var(--navy-dark));border-top:6px solid var(--blue);border-top-left-radius:90px;z-index:1}
.footer-brand{position:absolute;left:171px;top:3600px;font-family:"Montserrat",sans-serif;font-weight:700;font-size:40px;letter-spacing:1px;color:var(--white);line-height:1;z-index:3}
.footer-brand-sub{position:absolute;left:246px;top:3640px;font-weight:600;font-size:12px;color:var(--white);z-index:3}
.footer-copy{position:absolute;left:171px;top:3676px;width:330px;font-size:14px;line-height:26px;color:var(--white);z-index:3}
.footer-heading{position:absolute;top:3606px;font-family:"Jost",sans-serif;font-weight:500;font-size:23px;color:var(--lime);z-index:3}
.footer-item{position:absolute;font-size:13px;line-height:19px;color:var(--white);z-index:3}
.footer-icon{position:absolute;z-index:3}
.footer-social{position:absolute;top:3835px;width:20px;height:20px;border-radius:50%;background:var(--white);z-index:3}
.footer-legal{position:absolute;right:171px;top:3836px;font-size:13px;color:var(--white);z-index:3}
.footer-legal span{color:var(--lime)}
</style>
</head>
<body>

<!-- header -->
<div class="brand">BLUECREST</div>
<div class="brand-sub">Wound Care &amp; Hyperbarics</div>
<svg class="top-strip" viewBox="0 0 320 32" aria-hidden="true"><polygon points="5,0 320,0 320,32 28,32" fill="#0b2d55"/></svg>
<span class="social-dot" style="left:936px"></span>
<span class="social-dot" style="left:960px"></span>
<span class="social-dot" style="left:984px"></span>
<span class="social-dot" style="left:1008px"></span>
<a class="nav-link" style="left:626px">Home</a>
<span class="nav-active"></span>
<a class="nav-link" style="left:717px">About</a>
<a class="nav-link" style="left:809px">Blog</a>
<a class="btn" style="left:882px;top:44px;width:147px;height:46px">Learn More</a>

<!-- hero -->
<div class="hero-kicker">HYPERBARIC</div>
<h1 class="hero-title">OXYGEN<br>THERAPY</h1>
<div class="hero-sub">State of the Art Wound Care</div>
<a class="btn" style="left:171px;top:451px;width:148px;height:45px">Learn More</a>
<span class="slider-dot is-active" style="left:174px"></span>
<span class="slider-dot" style="left:210px"></span>
<span class="slider-dot" style="left:246px"></span>
<svg class="hero-art" viewBox="0 0 560 560" aria-hidden="true">
  <path d="M242 39 A240 240 0 0 0 202 500" fill="none" stroke="#0b2d55" stroke-width="15" stroke-linecap="round"/>
  <path d="M278 21 A250 250 0 0 1 535 356" fill="none" stroke="#0054AA" stroke-width="18" stroke-linecap="round"/>
  <path d="M531 323 A245 245 0 0 1 78 402" fill="none" stroke="#0677BA" stroke-width="14" stroke-linecap="round"/>
  <path d="M490 400 A235 235 0 0 1 340 505" fill="none" stroke="#CADEEF" stroke-width="10" stroke-linecap="round"/>
</svg>
<div class="photo hero-photo" role="img" aria-label="Clinician fitting a patient for hyperbaric oxygen therapy"></div>

<!-- welcome -->
<div class="photo welcome-photo" role="img" aria-label="Treatment room with two hyperbaric chambers"></div>
<div class="welcome-pre">Welcome to</div>
<h2 class="welcome-title">BLUECREST</h2>
<p class="welcome-copy">At Bluecrest Wound Care &amp; Hyperbarics we are committed to the highest level of care with state of the art technology. Our stand-alone clinics offer hyperbaric medicine, wound care and limb preservation in two conveniently located, outpatient settings.</p>
<a class="btn" style="left:608px;top:1018px;width:148px;height:46px">Learn More</a>

<!-- call band -->
<section class="call-band"></section>
<div class="call-title">Learn More <span>Today!</span></div>
<div class="call-sub">Give us a call to schedule a consult.</div>
<div class="call-number">Call: 555-014-2278</div>
<div class="frame" style="left:638px;top:1244px;width:406px;height:315px"></div>
<div class="photo call-photo" role="img" aria-label="Patient resting inside a hyperbaric chamber"></div>

<!-- team -->
<div class="blue-corner"></div>
<section class="team-section"></section>
<div class="frame" style="left:178px;top:1707px;width:396px;height:298px;z-index:3"></div>
<div class="photo team-photo" style="left:171px;background:linear-gradient(180deg,#ececeb,#d8d8d6 60%,#3b5a8f)" role="img" aria-label="Portrait of the chief executive officer"></div>
<div class="frame" style="left:633px;top:1707px;width:396px;height:298px;z-index:3"></div>
<div class="photo team-photo" style="left:626px;background:linear-gradient(135deg,#f1eeea,#d8d2cb 50%,#e58a33)" role="img" aria-label="Provider helping a patient into a hyperbaric chamber"></div>
<div class="team-name" style="left:171px">Daniel R. Whitford</div>
<div class="team-role" style="left:171px">Chief Executive Officer</div>
<p class="team-copy" style="left:171px;top:2105px;width:390px">Realizing the need for underutilized ancillary healthcare services like hyperbaric therapy, Daniel founded Bluecrest Wound Care and Hyperbarics</p>
<div class="team-name" style="left:626px">Your Provider</div>
<p class="team-copy" style="left:626px;top:2073px;width:410px">At Bluecrest, you will be treated by a highly-skilled provider, specially trained in wound care &amp; hyperbaric medicine.</p>
<a class="btn" style="left:504px;top:2195px;width:192px;height:49px;z-index:3">More About Us</a>

<!-- news -->
<section class="news-band"></section>
<h2 class="news-heading">Latest News</h2>
<div class="photo news-photo" style="left:171px;background:linear-gradient(135deg,#e8e2dc,#c9b9a6 50%,#d9c27a)" role="img" aria-label="Open hyperbaric chamber with treatment bed"></div>
<div class="photo news-photo" style="left:466px;background:linear-gradient(135deg,#dcdcdc,#a69684 50%,#e9d9a8)" role="img" aria-label="Patient relaxing in a hyperbaric chamber"></div>
<div class="photo news-photo" style="left:761px;background:linear-gradient(135deg,#eeeeee,#bfc3c6 50%,#8f9aa1)" role="img" aria-label="Multiplace hyperbaric chamber with control panel"></div>
<h3 class="news-title" style="left:171px">3 Tips To Prevent Diabetic Ulcers: When To Consider Hyperbaric Therapy</h3>
<h3 class="news-title" style="left:466px">Autism, Cerebral Palsy &amp; Fibromyalgia: 3 Lesser-Known Reasons To Consider HBOT</h3>
<h3 class="news-title" style="left:761px">How Many HBOT Sessions Do I Need? Treatment For Common Conditions</h3>
<p class="news-copy" style="left:171px">People with diabetes are more prone to infected wounds and diabetic ulcers. Hyperbaric therapy can help these infections heal faster.</p>
<p class="news-copy" style="left:466px">Hyperbaric oxygen therapy (HBOT) provides pure oxygen in a pressurized chamber, improving conditions such as autism, cerebral palsy</p>
<p class="news-copy" style="left:761px">HBOT continues to be an effective means of treating a range of common health issues. However, each condition needs several sessions to heal</p>
<a class="news-btn" style="left:171px">Read Now</a>
<a class="news-btn" style="left:466px">Read Now</a>
<a class="news-btn" style="left:761px">Read Now</a>

<!-- contact -->
<div class="footer-corner"></div>
<section class="contact-section"></section>
<h2 class="contact-heading">Contact Us</h2>
<div class="field" style="left:172px;top:3087px;width:271px;height:50px">First Name</div>
<div class="field" style="left:448px;top:3087px;width:271px;height:50px">Last Name</div>
<div class="field" style="left:172px;top:3141px;width:547px;height:50px">Email</div>
<div class="field" style="left:172px;top:3199px;width:547px;height:133px">How can we help?</div>
<a class="btn" style="left:172px;top:3359px;width:162px;height:49px;z-index:3">Submit Now</a>
<div class="frame" style="left:757px;top:3057px;width:268px;height:333px;z-index:3"></div>
<div class="photo contact-photo" role="img" aria-label="Smiling patient beside a hyperbaric chamber"></div>

<!-- footer -->
<footer class="site-footer"></footer>
<div class="footer-brand">BLUECREST</div>
<div class="footer-brand-sub">Wound Care &amp; Hyperbarics</div>
<p class="footer-copy">Constantly looking for ways to evolve the treatment of wounds and provide services that add value to the providers who refer patients to our facilities.</p>

<div class="footer-heading" style="left:546px">Contact Info</div>
<svg class="footer-icon" style="left:546px;top:3673px" width="14" height="18" viewBox="0 0 14 18" aria-hidden="true"><path d="M7 0C3.1 0 0 3 0 6.8 0 11.5 7 18 7 18s7-6.5 7-11.2C14 3 10.9 0 7 0zm0 9.3a2.5 2.5 0 1 1 0-5 2.5 2.5 0 0 1 0 5z" fill="#82FF00"/></svg>
<div class="footer-item" style="left:573px;top:3667px;width:260px">4820 Cedar Ridge Dr, Suite 210, Plano,<br>TX 75024</div>
<svg class="footer-icon" style="left:546px;top:3718px" width="16" height="16" viewBox="0 0 16 16" aria-hidden="true"><path d="M3.2 0.6l2.3 2.9c.4.5.3 1.1-.1 1.5L4.2 6.2c.9 2 3.5 4.6 5.6 5.6l1.2-1.2c.4-.4 1-.5 1.5-.1l2.9 2.3c.5.4.5 1.1.1 1.6l-1.3 1.3c-.8.8-2 1-3 .5C6.8 14.2 1.8 9.2.1 4.8-.3 3.8-.1 2.6.7 1.8L2 .5c.4-.4.9-.3 1.2.1z" fill="#82FF00"/></svg>
<div class="footer-item" style="left:573px;top:3716px">555-014-2278</div>
<svg class="footer-icon" style="left:546px;top:3752px" width="16" height="16" viewBox="0 0 16 16" aria-hidden="true"><rect x="0" y="3" width="16" height="13" rx="1.5" fill="#82FF00"/><rect x="3" y="0" width="10" height="5" fill="#82FF00"/><rect x="3" y="7" width="10" height="2" fill="#0b2d55"/><rect x="3" y="11" width="4" height="2" fill="#0b2d55"/><rect x="9" y="11" width="4" height="2" fill="#0b2d55"/></svg>
<div class="footer-item" style="left:573px;top:3751px">555-014-3391</div>

<div class="footer-heading" style="left:894px">Office Hours</div>
<div class="footer-item" style="left:895px;top:3664px">Monday- Friday</div>
<div class="footer-item" style="left:895px;top:3704px">8:00 am to 5:00 pm</div>

<span class="footer-social" style="left:171px"></span>
<span class="footer-social" style="left:215px"></span>
<span class="footer-social" style="left:263px"></span>
<span class="footer-social" style="left:314px"></span>
<div class="footer-legal">© 2022 <span>Bluecrest</span>&nbsp;&nbsp; All right reserved</div>

</body>
</html>
```